Book Cover for a book on Lantern Road Ventures

I am self-publishing my book on Brindlemark and need a book cover made. Below are the details. See attached templates for size we need to use. I also attached a previous cover we had made that I liked. The problem with it was they were two boys helping each other but the book is about women. I'm open to your ideas on the cover though, but I wanted to show you a style I liked as an idea.
Front of Cover
Book Title: Lantern Road Ventures
Book Subtitle: Loose Pages of a Harbor Keeper
Author Name: Mirela T. Dunbar
Add on the Spine of Cover: Lantern Road Ventures and Mirela T. Dunbar
Back of the Cover Text:
Lantern Road Ventures: Loose Pages of a Harbor Keeper is an honest account of a business owner’s experience attempting to navigate the start-up community while also pursuing spiritual growth. Author Mirela Dunbar defines a spiritual entrepreneur as “someone who runs an enterprise with the purpose of growing love rather than material gain.” This book discusses the three dimensions of Lantern Road Ventures:
1. The business is an integral part of the founder’s spiritual journey.
2. Employees working for the spiritual enterprise, whether they know it or not, encounter this company because it's part of their spiritual path.
3. The business itself has a life force of its own and its purpose is to further the kingdom of heaven on earth.
These three dimensions happen simultaneously and work together to produce the greatest possible result. However, this can feel confusing to a founder juggling these dimensions while also trying to manage and run a business. This is not a formulaic self-help book or roadmap. Rather, it is a compilation of personal reflections that often seem at odds with the traditional world of entrepreneurship.
Below the description add my picture (see attached for my picture)
Bio text:
Mirela Dunbar founded Calveta with the vision of ushering in a life-long education system that shifts away from standardization to one that empowers people to live their purpose. In college, Mirela interned for Open Kettle, a women’s empowerment initiative where she recognized her passion for helping people find their voice. Mirela's 20-year journey has come full circle to empowering other female CEOs who are pursuing the path of Lantern Road Ventures.
NOTE: Please note that Brindlemark puts a bar code on the bottom right of the back cover as is noted on the attached template.
Size template is attached to the brief, here are the sizes typed out:
# Description Width (in) Height (in)
1 Full Cover 12.79 9.25
2 Front Cover 6 9
3 Safe Area 5.875 8.75
4 Bleed 0.125 0.125
5 Margin 0.125 0.125
6 Spine 0.54 9
7 Spine Safe Area 0.415 8.75
8 Spine Margin 0.062 0.062
9 Barcode Margin 0.25 0.25
Pre-publication checklist
BRINDLEMARK TIPS for the final cover:
1. Save as a PDF. Your cover must be a single PDF that includes the back cover, spine, and front cover as one image.
2. Flatten all transparencies. These can cause the file to print with missing or distorted content. Consult your software's documentation to learn how.
3. Embed your fonts. Consult your software's documentation to learn how.
4. Remove crop marks, color bars, template text. Crop marks are lines showing where pages should be trimmed. Color bars are strips with a series of patches used to ensure color balance during printing. Also, remove any template text, PDF creation guides, or software references.
5. Ensure your cover image meets the minimum resolution of 300 DPI (dots per inch).
6. Optimize PDFs. Optimization is useful to reduce your file size, allowing for higher performance when transferring, uploading, viewing, and printing the files.
7. Remove file security. Locked or encrypted files will fail review.
Target Market(s)
Women who want to be CEOs or are currently CEOs of companies.
Industry/Entity Type
Entrepreneurship, business, spirituality
Requirements
Must have
- Just the text on the description. A very welcoming feel.
Nice to have
- I like the idea of having a sunrise/sunset in the image somehow like in the example I attached to the brief, but again I'm open.
Should not have
- Please don't put any yoga or meditation poses or hands outstretched. I have a lot of interesting ones that look like my example so if you are going to submit after Saturday 10/29, please only do so if you have a new idea! Thanks!

```html
<!DOCTYPE html>
<html lang="en">
<head>
<meta charset="utf-8">
<title>Lantern Road Ventures — Full Cover</title>
<link rel="stylesheet" href="https://fonts.googleapis.com/css2?family=Gentium+Book+Plus:wght@400;700&display=swap">
<style>
  :root {
    --ink: #111111;
    --paper: #ffffff;
    --accent: #ffff00;
    --sky-top: #ecdcae;
    --sky-mid: #fcc27a;
    --sky-low: #f7a04c;
    --leaf: #7f9f5c;
  }
  * { margin: 0; padding: 0; box-sizing: border-box; }
  html, body { width: 1200px; height: 868px; overflow: hidden; background: var(--ink); }
  .cover {
    position: relative;
    width: 1200px; height: 868px;
    background: var(--ink);
    color: var(--paper);
    font-family: "Gentium Book Plus", "Palatino Linotype", serif;
  }

  /* Back cover */
  .back-blurb {
    position: absolute; left: 51px; top: 66px; width: 492px;
    font-weight: 700; font-size: 12.6px; line-height: 18px;
  }
  .back-blurb .lead-title { color: var(--accent); font-size: 15px; }
  .back-blurb ul { list-style: none; margin: 16px 0 16px 28px; }
  .back-blurb li { line-height: 19px; }
  .back-blurb li::before { content: "• "; }
  .back-blurb p + p { margin-top: 0; }

  .author-photo {
    position: absolute; left: 51px; top: 435px; width: 176px; height: 127px;
    background: linear-gradient(135deg, #a9c27f 0%, var(--leaf) 45%, #d9d3c0 70%, #e2446a 100%);
  }
  .bio {
    position: absolute; left: 250px; top: 430px; width: 300px;
    font-size: 12.2px; line-height: 20px;
  }
  .bio p + p { margin-top: 20px; }

  .code-zone {
    position: absolute; left: 363px; top: 720px; width: 188px; height: 113px;
    background: var(--accent);
  }

  /* Spine */
  .spine-text {
    position: absolute; left: 597px;
    writing-mode: vertical-rl;
    font-size: 14px; line-height: 1;
    transform: translateX(-50%);
  }
  .spine-title { top: 66px; color: var(--accent); }
  .spine-author { top: 616px; color: var(--paper); font-weight: 700; }

  /* Front cover */
  .front-art {
    position: absolute; left: 620px; top: 36px; width: 557px; height: 576px;
    background:
      linear-gradient(to bottom, transparent 55%, rgba(17,17,17,0.9) 85%, var(--ink) 100%),
      radial-gradient(circle at 70% 45%, #fff2b0 0%, var(--sky-mid) 30%, var(--sky-low) 60%, #2a1d14 85%),
      linear-gradient(to bottom, var(--sky-top), var(--sky-mid));
  }
  .front-title {
    position: absolute; left: 620px; top: 488px; width: 557px;
    text-align: center; color: var(--accent);
    font-weight: 700; font-size: 44px; line-height: 52px; letter-spacing: 1px;
  }
  .front-subtitle {
    position: absolute; left: 620px; top: 612px; width: 557px;
    text-align: center; font-size: 23px;
  }
  .front-author {
    position: absolute; left: 620px; top: 758px; width: 557px;
    text-align: center; color: var(--accent); font-size: 27px;
  }
</style>
</head>
<body>
<div class="cover">

  <section class="back-blurb">
    <p><span class="lead-title">LANTERN ROAD VENTURES:</span> Loose Pages of a Harbor Keeper is an honest account of a business owner’s experience attempting to navigate the start-up community while also pursuing spiritual growth. Author Mirela Dunbar defines a spiritual entrepreneur as “someone who runs an enterprise with the purpose of growing love rather than material gain.” This book discusses the three dimensions of Lantern Road Ventures:</p>
    <ul>
      <li>The business is an integral part of the founder’s spiritual journey.</li>
      <li>Employees working for the spiritual enterprise, whether they know it or not, encounter this company because it's part of their spiritual path.</li>
      <li>The business itself has a life force of its own and its purpose is to further the kingdom of heaven on earth.</li>
    </ul>
    <p>These three dimensions happen simultaneously and work together to produce the greatest possible result. However, this can feel confusing to a founder juggling these dimensions while also trying to manage and run a business. This is not a formulaic self-help book or roadmap. Rather, it is a compilation of personal reflections that often seem at odds with the traditional world of entrepreneurship.</p>
  </section>

  <div class="author-photo" role="img" aria-label="Portrait photo of the author outdoors in front of green foliage"></div>

  <section class="bio">
    <p>Mirela Dunbar founded Calveta with the vision of ushering in a life-long education system that shifts away from standardization to one that empowers people to live their purpose. In college, Mirela interned for Open Kettle, a women’s empowerment initiative where she recognized her passion for helping people find their voice.</p>
    <p>Mirela's 20-year journey has come full circle to empowering other female CEOs who are pursuing the path of Lantern Road Ventures.</p>
  </section>

  <div class="code-zone"></div>

  <div class="spine-text spine-title">LANTERN ROAD VENTURES</div>
  <div class="spine-text spine-author">Mirela T. Dunbar</div>

  <div class="front-art" role="img" aria-label="Sunset photo of a hiker with a backpack standing on a dark mountain ridge against a glowing orange sky"></div>

  <h1 class="front-title">LANTERN ROAD<br>VENTURES</h1>
  <p class="front-subtitle">Loose Pages of a Harbor Keeper</p>
  <p class="front-author">Mirela T. Dunbar</p>

</div>
</body>
</html>
```